Marlow Fern Beauty Co.- Label template for Australian Small Batch Skincare company

Marlow Fern is a small batch, locally made, hand crafted beauty company which makes natural, ethically sourced beauty products for socially conscious consumers.
I need someone to design a product label template that have certain fields empty for example; ingredients, instructions, batch # and product name. I want to be able to fill these fields in later because I make a lot of products, and need flexibility. I want this as a template so I can fill in these fields before sending to printer.
I need two different label sizes;
-60ml amber jar. Internal Dimensions 5.5cm including lid x 50mm round diameter.
-30ml amber jar. Internal dimensions 5cm including lid x 40mm round diameter
Colour of Label: Either rose gold or white font. Depending on what looks the best. On Black background.
Target Market(s)
I am a professional working woman, wife and mother. I use products that are work for me and contain pure ingredients. I try to live a healthy lifestyle and I like products that support this.Financially secure women. Professionals. Might have own business. Majority are full time workers. $80k plus. Urban dwellers. Clean living supporters. Use organics. Have healthy diets. Mothers whose children are 10 years +.
Industry/Entity Type
Skin Care Product
Font styles to use
Other font styles liked:
- Typo (typewriter look font)
Requirements
Must have
- product label template that have certain fields empty for example; ingredients, instructions, batch # and product name. I want to be able to fill these fields in later because I make a lot of products, and need flexibility. I want this as a template so I can fill in these fields before sending to printer.
- Logo
- Ingredients- Blank field
- Space for Product name- Blank field
- Space for Product description – Blank field
- Space for Instructions- Blank field.
- Batch number (and a blank field for filling out later)
- 60 or 30 ml
- Tagline – nurturing kind hearts, fierce minds, & brave spirits
- Hand crafted with love in Melbourne
- Website- www.marlowfernbeautycompany.example
- Black background, Rose gold font. Typo font. (Font that looks like typewriter)
Nice to have
- Art Deco design elements. Rose gold on black background. I want this label to represent my artisan approach to skin care formulation and production. Everything is handmade by me.
Should not have
- Mass production feel

```html
<!DOCTYPE html>
<html lang="en">
<head>
<meta charset="utf-8">
<title>Marlow Fern Beauty Co. – Jar Label Template</title>
<link rel="stylesheet" href="https://fonts.googleapis.com/css2?family=Special+Elite&display=swap">
<style>
  :root {
    --page: #f2f2f2;
    --label-black: #1e1c1c;
    --logo-panel: #2b2624;
    --rose-gold: #cfa189;
    --rose-gold-soft: #b88a73;
    --rose-gold-dim: #8a6655;
    --ink-light: #ece4df;
  }
  * { margin: 0; padding: 0; box-sizing: border-box; }
  html, body {
    width: 1001px; height: 1200px; overflow: hidden;
    background: var(--page);
  }
  body { position: relative; font-family: "Special Elite", "Courier New", monospace; }

  .jar-label {
    position: absolute; left: 56px; top: 444px;
    width: 890px; height: 312px;
    background: var(--label-black);
    color: var(--ink-light);
  }
  .label-frame { position: absolute; inset: 0; }
  .label-frame .rule { stroke: var(--rose-gold-soft); fill: none; }

  .logo-panel {
    position: absolute; left: 317px; top: 2px; width: 252px; height: 122px;
    background: var(--logo-panel);
    display: flex; align-items: center; justify-content: center;
    text-align: center;
  }
  .brand-name {
    font-size: 25px; line-height: 1.15; color: var(--rose-gold);
    letter-spacing: 1px; white-space: nowrap;
  }

  .ornament {
    position: absolute; background: var(--rose-gold-dim); border-radius: 12px; opacity: .85;
  }
  .ornament-crest { left: 374px; top: 128px; width: 143px; height: 28px; }
  .ornament-scroll-left { left: 268px; top: 222px; width: 70px; height: 26px; }
  .ornament-scroll-right { left: 554px; top: 222px; width: 70px; height: 26px; }
  .ornament-sprig { left: 702px; top: 224px; width: 93px; height: 22px; }

  .product-name {
    position: absolute; left: 336px; width: 220px; top: 176px;
    text-align: center; font-size: 17px; line-height: 20px; color: var(--rose-gold);
    white-space: nowrap;
  }
  .product-description {
    position: absolute; left: 346px; width: 200px; top: 212px;
    border-top: 1px solid var(--rose-gold-soft);
    border-bottom: 1px solid var(--rose-gold-soft);
    padding: 5px 0 3px;
    text-align: center; font-size: 9.5px; line-height: 14px; color: var(--ink-light);
    white-space: nowrap;
  }
  .volume {
    position: absolute; left: 396px; width: 100px; top: 260px;
    text-align: center; font-size: 13px; line-height: 16px; color: var(--rose-gold);
  }

  .details { position: absolute; left: 26px; top: 35px; width: 262px; font-size: 10.5px; line-height: 14.4px; }
  .field-label { display: flex; align-items: center; color: var(--ink-light); }
  .field-label::after {
    content: ""; display: block; width: 94px; height: 1px; margin-left: 6px;
    background: var(--rose-gold-soft);
  }
  .field-body { color: var(--ink-light); opacity: .9; margin-bottom: 8px; white-space: nowrap; }
  .field-batch { margin-top: 2px; }

  .tagline-frame {
    position: absolute; left: 650px; top: 50px; width: 196px; height: 106px;
    border: 1.5px solid var(--rose-gold-soft); border-radius: 40px / 30px;
    display: flex; align-items: center; justify-content: center;
    text-align: center; font-size: 12px; line-height: 17px; color: var(--rose-gold);
  }
  .origin {
    position: absolute; left: 640px; width: 216px; top: 176px;
    text-align: center; font-size: 12px; line-height: 17px; color: var(--rose-gold);
    white-space: nowrap;
  }
  .website {
    position: absolute; left: 622px; width: 248px; top: 261px;
    text-align: center; font-size: 10.5px; line-height: 14px; color: var(--ink-light);
    white-space: nowrap;
  }
</style>
</head>
<body>
  <section class="jar-label" aria-label="60ml jar label template">
    <svg class="label-frame" width="890" height="312" viewBox="0 0 890 312" aria-hidden="true">
      <path class="rule" stroke-width="4" d="M317 13 H26 M569 13 H864 M877 26 V286 M864 299 H26 M13 286 V26"/>
      <path class="rule" stroke-width="1.5" d="M317 20 H20 V292 H870 V20 H569"/>
      <rect x="6" y="6" width="14" height="14" fill="var(--rose-gold-dim)"/>
      <rect x="870" y="6" width="14" height="14" fill="var(--rose-gold-dim)"/>
      <rect x="6" y="292" width="14" height="14" fill="var(--rose-gold-dim)"/>
      <rect x="870" y="292" width="14" height="14" fill="var(--rose-gold-dim)"/>
    </svg>

    <div class="logo-panel">
      <p class="brand-name">Marlow Fern<br>Beauty Co.</p>
    </div>
    <div class="ornament ornament-crest" role="img" aria-label="Rose gold filigree flourish"></div>

    <div class="details">
      <p class="field-label">Ingredients:</p>
      <p class="field-body">Lorem ipsum dolor sit amet, consectetur<br>adipiscing elit, sed do eiusmod tempor<br>incididunt ut labore et dolore magna<br>aliqua. Ut enim ad minim veniam, quis<br>nostrud exercitation ullamco laboris</p>
      <p class="field-label">Instructions:</p>
      <p class="field-body">Duis aute irure dolor in reprehenderit<br>in voluptate velit esse cillum dolore eu<br>fugiat nulla pariatur. Excepteur sint<br>occaecat cupidatat non proident, sunt in<br>culpa qui officia deserunt mollit anim<br>id est laborum</p>
      <p class="field-label field-batch">Batch #:</p>
    </div>

    <p class="product-name">Product Name</p>
    <div class="ornament ornament-scroll-left" role="img" aria-label="Rose gold scroll flourish"></div>
    <p class="product-description">Product description Product<br>description Product description</p>
    <div class="ornament ornament-scroll-right" role="img" aria-label="Rose gold scroll flourish"></div>
    <p class="volume">60ml</p>

    <div class="tagline-frame">
      <p>nurturing<br>kind hearts,<br>fierce minds,<br>&amp; brave spirits</p>
    </div>
    <p class="origin">Hand crafted with love<br>in Melbourne</p>
    <div class="ornament ornament-sprig" role="img" aria-label="Rose gold floral sprig ornament"></div>
    <p class="website">www.marlowfernbeautycompany.example</p>
  </section>
</body>
</html>
```